Landing page design for secure cloud backup web application

We would like a landing page design for our web application. Our app allows users to securely save their data in the cloud using their existing storage providers, such as stashPod, Pila, Ferravex Haze Locker, Quorble vault and Tandrix Pax vault.
We make it extremely easy for individual users and small businesses to deploy sophisticated client-side encryption without having to worry about the technical complexity inherent in such solutions.
We already have the logo design done - I am attaching the logo file. We also have a preliminary website drafted at www.plimva.com
I need a good color scheme, typography, layout, along with templates for 'help', 'about', 'privacy notice', 'legal' and such typical sub-pages
The design should be uncluttered, clean and minimalist

Target Market(s)

Individuals and medium/small businesses that are conscious about the security of their data in the cloud

Coding

Coded - Design and coding required

Number of Pages Required

4 page

Font styles to use
Sans Serif

Requirements
Must have
• Section where I describe the product along with pictures/images
• section for explainer video on main page
• FAQ section
• Help section
• Legal/privacynotice/terms of use section
• feedback section
Nice to have
• see existing draft site www.plimva.com for content guidelines only.
• see attached logo files for color scheme guidelines - I am willing to accept change in the logo color if necessary to create a better web site look and feel
• Fonts on page should match font in the logo

```html
<!DOCTYPE html>
<html lang="en">
<head>
<meta charset="utf-8">
<title>Plimva – Secure Cloud Storage</title>
<link rel="stylesheet" href="https://fonts.googleapis.com/css2?family=Roboto:wght@300;400;500;700&display=swap">
<style>
:root{
  --orange:#f7941d;
  --orange-deep:#f08a12;
  --coral:#e8584c;
  --brown:#3b1f0e;
  --text:#555;
  --muted:#777;
  --grey-bg:#f0f0f0;
  --icon-dark:#4a4a4a;
  --help:#7a7a7a;
  --feedback:#5e5e5e;
  --white:#fff;
}
*{box-sizing:border-box;margin:0;padding:0}
html,body{width:722px;height:1200px;overflow:hidden;background:var(--white)}
body{position:relative;font-family:'Roboto',Arial,sans-serif;color:var(--text)}
.abs{position:absolute}

/* header */
.site-header{position:absolute;left:0;top:0;width:722px;height:54px;background:var(--white)}
.brand{position:absolute;left:45px;top:14px;display:flex;align-items:center;gap:6px;font-size:22px;font-weight:500;color:#444;letter-spacing:.5px}
.brand-dot{width:18px;height:18px;border-radius:50%;background:#444}
.main-nav a{position:absolute;top:23px;font-size:8.5px;color:#333;text-decoration:none}
.signup{position:absolute;left:578px;top:17px;width:99px;height:21px;background:var(--coral);color:var(--white);font-size:9px;font-weight:500;text-align:center;line-height:21px;letter-spacing:.3px}

/* hero */
.hero{position:absolute;left:0;top:54px;width:722px;height:312px;background:radial-gradient(ellipse at 40% 45%,#fba43a 0%,var(--orange) 45%,var(--orange-deep) 100%)}
.hero-brand{position:absolute;left:45px;top:60px;display:flex;align-items:center;gap:10px;font-size:38px;font-weight:500;color:var(--white)}
.hero-brand-dot{width:34px;height:34px;border-radius:50%;border:5px solid var(--white)}
.hero-text{position:absolute;left:47px;top:152px;width:295px;font-size:8.8px;line-height:15.6px;color:var(--white);text-align:justify}
.hero-arrow{position:absolute;top:230px;width:22px;height:22px;border-radius:50%;background:var(--white)}
.hero-screen{position:absolute;left:402px;top:48px;width:275px;height:228px;border-radius:6px;background:linear-gradient(180deg,#2a2a2a 0%,#1a1a1a 100%);padding:7px}
.hero-screen-inner{width:100%;height:100%;background:linear-gradient(180deg,#f4f1e6,#efe8d6)}
.hero-stand{position:absolute;left:500px;top:276px;width:80px;height:52px;background:linear-gradient(180deg,#d8d8d8,#bdbdbd);clip-path:polygon(30% 0,70% 0,100% 100%,0 100%)}

/* features */
.section-title{position:absolute;left:0;width:722px;text-align:center;font-size:19.5px;font-weight:400;color:var(--brown);letter-spacing:.4px}
.title-rule{position:absolute;left:326px;top:435px;width:70px;height:2px;background:var(--orange)}
.feature{position:absolute;top:458px;width:140px;text-align:center}
.feature-icon{width:53px;height:53px;border-radius:50%;margin:0 auto;display:flex;align-items:center;justify-content:center;background:var(--icon-dark)}
.feature-icon.is-accent{background:var(--orange)}
.feature h3{margin-top:17px;font-size:10px;font-weight:500;color:#222;letter-spacing:.3px}
.feature p{margin-top:7px;font-size:8px;line-height:13.5px;color:var(--muted);text-align:justify;text-align-last:center}

/* products */
.products{position:absolute;left:0;top:610px;width:722px;height:236px;background:var(--grey-bg)}
.product-card{position:absolute;top:68px;width:301px;height:124px;background:var(--white);display:flex}
.product-media{width:140px;height:124px}
.product-body{padding:15px 15px 0 15px;width:161px}
.product-body h4{font-size:11.5px;font-weight:400;color:var(--orange)}
.product-body p{margin-top:8px;font-size:7.6px;line-height:13.5px;color:var(--muted);text-align:justify}
.btn{display:block;background:var(--orange);color:var(--white);font-size:8.5px;text-align:center;text-decoration:none}
.product-body .btn{margin-top:9px;width:78px;height:24px;line-height:24px}
.dots{position:absolute;left:349px;top:820px;display:flex;gap:4px}
.dots span{width:5px;height:5px;border-radius:50%;background:#ccc}
.dots span.is-active{background:#666}

/* faq */
.faq-title{position:absolute;left:45px;top:873px;font-size:19.5px;font-weight:400;color:var(--brown)}
.faq-q{position:absolute;left:45px;font-size:11px;color:var(--orange)}
.faq-a{position:absolute;left:45px;width:406px;font-size:7.8px;line-height:13.6px;color:var(--text)}
.view-all{position:absolute;left:45px;top:1063px;width:91px;height:25px;line-height:25px}
.side-box{position:absolute;left:478px;width:200px;padding:12px;color:var(--white);border:1px solid #555}
.side-box h5{display:flex;align-items:center;gap:5px;font-size:13px;font-weight:500}
.side-box p{font-size:8px;line-height:13.6px;text-align:justify}
.help{top:878px;height:86px;background:var(--help)}
.feedback{top:977px;height:108px;background:var(--feedback)}

/* footer */
.site-footer{position:absolute;left:0;top:1132px;width:722px;height:68px;background:linear-gradient(180deg,#5b5b5b,#3c3c3c)}
.footer-brand{position:absolute;left:45px;top:25px;display:flex;align-items:center;gap:5px;font-size:14px;font-weight:500;color:var(--white)}
.footer-brand span{width:12px;height:12px;border-radius:50%;background:var(--white)}
.footer-links{position:absolute;left:93px;top:32px;font-size:8.4px;color:var(--white)}
.footer-links .sep{margin:0 6px}
.social{position:absolute;left:582px;top:36px;display:flex;gap:4px}
.social span{width:17px;height:17px;border-radius:50%;background:var(--white)}
</style>
</head>
<body>

<header class="site-header">
  <div class="brand"><span class="brand-dot"></span>Plimva</div>
  <nav class="main-nav">
    <a style="left:240px" href="#">Home</a>
    <a style="left:292px" href="#">About Us</a>
    <a style="left:356px" href="#">FAQ's</a>
    <a style="left:405px" href="#">Contact Us</a>
    <a style="left:474px" href="#">Developer</a>
    <a style="left:536px" href="#">Log In</a>
  </nav>
  <a class="signup" href="#">Sign Up FREE</a>
</header>

<section class="hero">
  <div class="hero-brand"><span class="hero-brand-dot"></span>Plimva</div>
  <p class="hero-text">You have data you want to keep to yourself. You want it safe in the cloud so you can get at it anywhere. You don't want to mess with encryption keys yet you want to keep hackers and snoops out. You know it shouldn't be so hard.You're right.</p>
  <div class="hero-arrow" style="left:46px">
    <svg width="22" height="22" viewBox="0 0 22 22"><path d="M12.5 7 8.5 11l4 4" fill="none" stroke="#555" stroke-width="1.8"/></svg>
  </div>
  <div class="hero-arrow" style="left:72px">
    <svg width="22" height="22" viewBox="0 0 22 22"><path d="M9.5 7l4 4-4 4" fill="none" stroke="#555" stroke-width="1.8"/></svg>
  </div>
  <div class="hero-screen"><div class="hero-screen-inner" role="img" aria-label="Desktop monitor showing the Plimva secure storage web app file list"></div></div>
  <div class="hero-stand"></div>
</section>

<h2 class="section-title" style="top:404px">Keep your data private without breaking a sweat</h2>
<div class="title-rule"></div>

<div class="feature" style="left:43px">
  <div class="feature-icon is-accent">
    <svg width="22" height="22" viewBox="0 0 24 24"><path d="M12 20s-8-5-8-11a4.5 4.5 0 0 1 8-2.6A4.5 4.5 0 0 1 20 9c0 6-8 11-8 11z" fill="none" stroke="#fff" stroke-width="2"/></svg>
  </div>
  <h3>USE YOUR CLOUD</h3>
  <p>Plimva lets you use the accounts you you already have and trust, such as Pila, stashPod</p>
</div>
<div class="feature" style="left:209px">
  <div class="feature-icon">
    <svg width="22" height="22" viewBox="0 0 24 24"><rect x="10" y="3" width="4" height="12" fill="#fff"/><rect x="10" y="17" width="4" height="4" fill="#fff"/></svg>
  </div>
  <h3>ZERO KNOWLEDGE</h3>
  <p>When it comes to data security, zero knowledge is a good thing. No one, including Plimva</p>
</div>
<div class="feature" style="left:372px">
  <div class="feature-icon">
    <svg width="22" height="22" viewBox="0 0 24 24"><path d="M4 11h4v9H4zM8 11l4-7c1.5 0 2 1 2 2l-1 4h6c1 0 2 1 1.6 2.2L19 19c-.3.7-1 1-1.6 1H8" fill="none" stroke="#fff" stroke-width="1.7" stroke-linejoin="round"/></svg>
  </div>
  <h3>EASY to USE</h3>
  <p>Plimva is completely browser based. So there is no software to install, no updates to perform.</p>
</div>
<div class="feature" style="left:536px">
  <div class="feature-icon">
    <svg width="22" height="22" viewBox="0 0 24 24"><path d="M12 22s-6-7-6-12a6 6 0 0 1 12 0c0 5-6 12-6 12z" fill="#fff"/><circle cx="12" cy="10" r="2.2" fill="#4a4a4a"/></svg>
  </div>
  <h3>ACCESS ANYWHERE</h3>
  <p>Your data is accessibe from anywhere you can use a browser and access the internet.</p>
</div>

<section class="products">
  <h2 class="section-title" style="top:26px">Featured Products</h2>
  <article class="product-card" style="left:48px">
    <div class="product-media" role="img" aria-label="Phone with a cloud storage app on a wooden desk beside a laptop and coffee" style="background:linear-gradient(135deg,#8a6a4a,#b08660 50%,#5a4230)"></div>
    <div class="product-body">
      <h4>Product Name</h4>
      <p>Neque porro quisquam est qui dolorem ipsum quia dolor sit amet consectetur, adipisci velit.</p>
      <a class="btn" href="#">Get Detail</a>
    </div>
  </article>
  <article class="product-card" style="left:373px">
    <div class="product-media" role="img" aria-label="Close-up of colourful app icons on a tablet screen" style="background:linear-gradient(135deg,#1b1f2e,#3a2a4a 50%,#14243a)"></div>
    <div class="product-body">
      <h4>Product Name</h4>
      <p>Neque porro quisquam est qui dolorem ipsum quia dolor sit amet consectetur, adipisci velit.</p>
      <a class="btn" href="#">Get Detail</a>
    </div>
  </article>
</section>
<div class="dots"><span class="is-active"></span><span></span><span></span></div>

<h2 class="faq-title">FAQ's</h2>
<h3 class="faq-q" style="top:912px">Q: Where is my data stored?</h3>
<p class="faq-a" style="top:930px">Your data is stored on your accounts on two or more of the following storage providers - Pila, stashPod, Quorble vault, Tandrix Pax vault and Ferravex Haze Locker. Plimva does not provide storage. When you set up your account with Plimva, you will select the storage providers.</p>
<h3 class="faq-q" style="top:990px">Q: How do you ensure that no one else can see my data?</h3>
<p class="faq-a" style="top:1008px">We use the latest in-browser AES-256 bit cipher to encrypt your files with a randomly generated key. Then your file contents are split and separate chunks are stored on the storage providers. This ensure that even if any of the storage providers gets hacked or compromised.</p>
<a class="btn view-all" href="#">View All</a>

<aside class="side-box help">
  <h5><svg width="13" height="13" viewBox="0 0 24 24"><circle cx="12" cy="12" r="9" fill="none" stroke="#fff" stroke-width="2.4"/><circle cx="12" cy="12" r="4" fill="none" stroke="#fff" stroke-width="2.4"/><path d="M5.5 5.5l3.7 3.7M18.5 5.5l-3.7 3.7M5.5 18.5l3.7-3.7M18.5 18.5l-3.7-3.7" stroke="#fff" stroke-width="2.4"/></svg>Help</h5>
  <p style="margin-top:8px">Neque porro quisquam est qui dolorem ipsum quia dolor sit amet, consectetur, adipisci velitNeque porro quisquam.</p>
</aside>
<aside class="side-box feedback">
  <h5><svg width="13" height="13" viewBox="0 0 24 24"><path d="M10 14a4 4 0 0 0 5.7 0l3.5-3.5a4 4 0 0 0-5.7-5.7L12 6.3M14 10a4 4 0 0 0-5.7 0l-3.5 3.5a4 4 0 0 0 5.7 5.7l1.5-1.5" fill="none" stroke="#fff" stroke-width="2.2"/></svg>Feedback</h5>
  <p style="margin-top:9px">» &nbsp;Neque porro quisquam est qui dolorem ipsum velitNeque porro quisquam.</p>
  <p style="margin-top:8px">» &nbsp;Neque porro quisquam est qui dolorem ipsum velitNeque porro quisquam.</p>
</aside>

<footer class="site-footer">
  <div class="footer-brand"><span></span></div>
  <div class="footer-links">Legal<span class="sep">|</span>Privacy notice<span class="sep" style="margin:0 9px">|</span>Terms of use section</div>
  <div class="social"><span></span><span></span><span></span><span></span><span></span></div>
</footer>

</body>
</html>
```